Tarnby Group letterhead

Hi,

I need a letterhead template created for our business. This should be done in word format and A4 size. The images need to not move in the template ie when I am adding writing in etc. and should flow on when I get to a second page.

I have attached our logo templates below.

Other details to include on the letterhead somewhere are:

0438 915 267
Max@Tarnbyelectrical.example.au
PO Box 817 Marrowvale NSW 2190
ABN: 57 318 962 407

Thanks!

```html
<!DOCTYPE html>
<html lang="en">
<head>
<meta charset="utf-8">
<title>Tarnby Group Letterhead</title>
<link href="https://fonts.googleapis.com/css2?family=Poppins:wght@400;500;600;700&display=swap" rel="stylesheet">
<style>
  :root {
    --ink: #2b2a2b;
    --orange: #e5532a;
    --paper: #ffffff;
    --faint: #ebebeb;
    --muted: #c4c4c4;
    --rule: #2b2a2b;
  }
  * { box-sizing: border-box; margin: 0; padding: 0; }
  html, body { width: 1200px; height: 845px; overflow: hidden; background: var(--paper); }
  body { font-family: "Poppins", sans-serif; color: var(--ink); }
  .artboard {
    position: relative; width: 1200px; height: 845px;
    border: 1px solid #555; background: var(--paper);
  }
  .sheet {
    position: absolute; top: 72px; width: 496px; height: 700px;
    border: 1px solid var(--rule); background: var(--paper); overflow: hidden;
  }
  .sheet--letter { left: 98px; }
  .sheet--continuation { left: 606px; }

  .brand { position: absolute; top: 15px; left: 0; width: 100%; text-align: center; }
  .brand__dot {
    display: block; width: 54px; height: 54px; margin: 0 auto;
    border: 4px solid var(--ink); border-radius: 50%;
  }
  .brand__name {
    display: block; margin-top: 12px; font-size: 20px; font-weight: 700;
    letter-spacing: 1.5px; text-transform: uppercase; color: var(--ink);
  }

  .band { position: absolute; left: 0; width: 100%; }
  .band--dark-top { top: 133px; height: 14px; background: var(--ink); }
  .band--orange-top { top: 149px; height: 7px; background: var(--orange); }
  .band--orange-bottom { top: 667px; height: 10px; background: var(--orange); }
  .band--dark-bottom { top: 679px; height: 22px; background: var(--ink); }

  .watermark { position: absolute; }
  .sheet--letter .watermark { left: 126px; top: 288px; }
  .sheet--continuation .watermark { left: 126px; top: 290px; }

  .recipient, .date, .body-copy, .signature, .contact {
    position: absolute; font-size: 10px; line-height: 15.2px;
  }
  .recipient { left: 36px; top: 178px; font-weight: 600; }
  .date { right: 36px; top: 178px; font-weight: 600; }
  .body-copy { left: 36px; width: 424px; top: 256px; }
  .body-copy p { text-align: justify; margin-bottom: 15.2px; }
  .signature { left: 59px; top: 606px; font-size: 9px; line-height: 20px; }
  .signature__line { color: var(--muted); }
  .signature__name { font-weight: 600; }
  .contact { right: 36px; top: 585px; text-align: right; font-size: 9px; line-height: 14px; font-weight: 600; }

  .writing-area {
    position: absolute; left: 36px; top: 184px; width: 424px; height: 456px;
    border: 1px dotted #b9b9b9;
  }
</style>
</head>
<body>
<div class="artboard">

  <section class="sheet sheet--letter">
    <header class="brand">
      <span class="brand__dot"></span>
      <span class="brand__name">Tarnby Group</span>
    </header>
    <div class="band band--dark-top"></div>
    <div class="band band--orange-top"></div>

    <svg class="watermark" width="244" height="244" viewBox="0 0 244 244" aria-hidden="true">
      <circle cx="122" cy="122" r="112" fill="none" stroke="var(--faint)" stroke-width="19"/>
    </svg>

    <div class="recipient">
      Your Name<br>Your position<br>Company Name<br>Company Address
    </div>
    <div class="date">Sunday,17 November 2000</div>

    <div class="body-copy">
      <p>Lorem ipsum dolor sit amet. Dolor ea eos lorem. At sadipscing doming iriure et sanctus. Diam eros gubergren rebum eu. Esse ut dolore ut diam ea iriure at. Voluptua diam ut at no suscipit. Tempor aliquam vel sit. Diam sed rebum ea invidunt zzril in. Amet et justo sanctus. Amet nulla justo lorem vel euismod aliquyam. In et dolor iusto. Ea sanctus sit eirmod aliquip erat dolore nam.</p>
      <p>Dolor dolores eu sadipscing sit. Blandit facilisis aliquam velit. Praesent ea et takimata sanctus. Et no duo at kasd. Sed eos adipiscing eu invidunt accumsan dolore. Ex accusam sit erat dolor. Sanctus blandit ea nulla stet. Zzril nam eum diam sed no takimata. Dolores blandit ipsum gubergren dignissim sadipscing. Kasd duo gubergren vel lorem consetetur labore elitr. Tincidunt ipsum magna ea. Sea velit diam eros nonumy sed amet erat. Stet amet erat no kasd ut clita ipsum. Et vel lorem rebum eirmod duo. Takimata dolore accumsan. Aliquyam erat commodo tempor enim ut. Erat dolor invidunt magna duo sadipscing ea tempor. Et ut diam ea tempor duis dignissim.</p>
      <p>Sit dolor sit sanctus at dolore. Erat diam id assum vel. Consetetur erat hendrerit. Diam et nonumy consequat consetetur dolor. Lorem aliquip vero ex diam erat dignissim. Sed voluptua sanctus lorem luptatum invidunt dolor. No velit rebum erat vulputate sed rebum et. Facilisis mazim id nostrud diam et nostrud invidunt. gubergren ut. Dignissim takimata veniam. Vero at est</p>
    </div>

    <div class="signature">
      <div class="signature__line">SIGN HERE</div>
      <div class="signature__name">Your Name</div>
    </div>

    <address class="contact" style="font-style:normal">
      0438 915 267<br>
      Max@Tarnbyelectrical.example.au<br>
      PO Box 817 Marrowvale NSW 2190<br>
      ABN: 57 318 962 407
    </address>

    <div class="band band--orange-bottom"></div>
    <div class="band band--dark-bottom"></div>
  </section>

  <section class="sheet sheet--continuation">
    <header class="brand">
      <span class="brand__dot"></span>
      <span class="brand__name">Tarnby Group</span>
    </header>
    <div class="band band--dark-top"></div>
    <div class="band band--orange-top"></div>

    <div class="writing-area"></div>
    <svg class="watermark" width="244" height="244" viewBox="0 0 244 244" aria-hidden="true">
      <circle cx="122" cy="122" r="112" fill="none" stroke="var(--faint)" stroke-width="19"/>
    </svg>

    <div class="band band--orange-bottom"></div>
    <div class="band band--dark-bottom"></div>
  </section>

</div>
</body>
</html>
```